Construction business card

I need a new business card, they can connect with my logo, brand.
What we do is residential house , design and build
I like: Navy blue / black
I attached our logo, brand,
and, some idea for business card.

```html
<!DOCTYPE html>
<html lang="en">
<head>
<meta charset="utf-8">
<title>Northgate Building Group – Business Card</title>
<link rel="stylesheet" href="https://fonts.googleapis.com/css2?family=Montserrat:wght@600;800&family=Open+Sans:wght@400;600&display=swap">
<style>
  :root {
    --navy: #1f3a63;
    --navy-deep: #172d4f;
    --copper: #c47a4b;
    --paper: #f8f6f2;
    --ink: #2b3442;
    --backdrop: #e6e4e0;
    --rule: #d9d3ca;
  }
  * { box-sizing: border-box; margin: 0; padding: 0; }
  html, body { width: 1200px; height: 1200px; overflow: hidden; }
  body {
    background: var(--backdrop);
    display: flex;
    flex-direction: column;
    align-items: center;
    justify-content: center;
    gap: 60px;
    font-family: "Open Sans", sans-serif;
  }
  .card {
    width: 900px;
    height: 514px;
    position: relative;
    overflow: hidden;
    box-shadow: 0 10px 28px rgba(0,0,0,0.12);
  }
  .card::after {
    content: "";
    position: absolute;
    left: 0; right: 0; bottom: 0;
    height: 10px;
    background: var(--copper);
  }

  /* Front */
  .card-front {
    background: var(--navy);
    display: flex;
    flex-direction: column;
    align-items: center;
    justify-content: center;
    gap: 22px;
  }
  .brand-row { display: flex; align-items: center; gap: 24px; }
  .brand-square { width: 58px; height: 58px; background: var(--copper); flex: none; }
  .brand-name {
    font-family: "Montserrat", sans-serif;
    font-weight: 800;
    font-size: 50px;
    letter-spacing: 1px;
    text-transform: uppercase;
    color: var(--copper);
    line-height: 1;
  }
  .front-tagline {
    font-family: "Montserrat", sans-serif;
    font-weight: 600;
    font-size: 19px;
    letter-spacing: 6px;
    text-transform: uppercase;
    color: var(--copper);
  }

  /* Back */
  .card-back {
    background: var(--paper);
    padding: 52px 60px 40px;
    color: var(--ink);
  }
  .back-header { display: flex; align-items: center; gap: 22px; }
  .back-header .brand-square { width: 64px; height: 64px; }
  .back-name {
    font-family: "Montserrat", sans-serif;
    font-weight: 800;
    font-size: 40px;
    text-transform: uppercase;
    color: var(--navy);
    line-height: 1.05;
  }
  .back-tagline {
    font-family: "Montserrat", sans-serif;
    font-weight: 600;
    font-size: 16px;
    letter-spacing: 5px;
    text-transform: uppercase;
    color: var(--navy);
    margin-top: 6px;
  }
  .back-body {
    display: grid;
    grid-template-columns: 1fr 1fr;
    gap: 40px;
    margin-top: 46px;
  }
  .person-name {
    font-family: "Montserrat", sans-serif;
    font-weight: 800;
    font-size: 26px;
    text-transform: uppercase;
    color: var(--navy);
  }
  .person-role {
    font-size: 15px;
    letter-spacing: 2px;
    text-transform: uppercase;
    color: var(--ink);
    margin-bottom: 18px;
  }
  .contact-list { list-style: none; display: flex; flex-direction: column; gap: 12px; }
  .contact-list li { display: flex; align-items: flex-start; gap: 12px; font-size: 17px; line-height: 1.3; }
  .contact-list svg { width: 20px; height: 20px; flex: none; margin-top: 1px; }
  .contact-right { border-left: 1px solid var(--rule); padding-left: 40px; padding-top: 6px; }
  .social-dot { width: 18px; height: 18px; border-radius: 50%; background: var(--navy); flex: none; margin-top: 2px; }
</style>
</head>
<body>

  <section class="card card-front" aria-label="Card front">
    <div class="brand-row">
      <span class="brand-square"></span>
      <span class="brand-name">Northgate Building Group</span>
    </div>
    <p class="front-tagline">Premier Construction Services</p>
  </section>

  <section class="card card-back" aria-label="Card back">
    <header class="back-header">
      <span class="brand-square"></span>
      <div>
        <h1 class="back-name">Northgate Building Group</h1>
        <p class="back-tagline">Building Your Vision</p>
      </div>
    </header>

    <div class="back-body">
      <div class="contact-left">
        <h2 class="person-name">Daniel Hayes</h2>
        <p class="person-role">Executive Director</p>
        <ul class="contact-list">
          <li>
            <svg viewBox="0 0 24 24" fill="none" stroke="#c47a4b" stroke-width="2"><circle cx="12" cy="12" r="9"/><path d="M3 12h18M12 3c3 3 3 15 0 18M12 3c-3 3-3 15 0 18"/></svg>
            www.northgatebuild.com
          </li>
          <li>
            <svg viewBox="0 0 24 24" fill="none" stroke="#c47a4b" stroke-width="2" stroke-linejoin="round"><path d="M5 3h4l2 5-2.5 1.5a11 11 0 0 0 6 6L16 13l5 2v4a2 2 0 0 1-2 2A16 16 0 0 1 3 5a2 2 0 0 1 2-2z"/></svg>
            (555) 284-7310
          </li>
          <li><span class="social-dot"></span>@NorthgateBuild</li>
        </ul>
      </div>

      <div class="contact-right">
        <ul class="contact-list">
          <li>
            <svg viewBox="0 0 24 24" fill="none" stroke="#c47a4b" stroke-width="2" stroke-linejoin="round"><path d="M5 3h4l2 5-2.5 1.5a11 11 0 0 0 6 6L16 13l5 2v4a2 2 0 0 1-2 2A16 16 0 0 1 3 5a2 2 0 0 1 2-2z"/></svg>
            (555) 284-7310
          </li>
          <li>
            <svg viewBox="0 0 24 24" fill="none" stroke="#c47a4b" stroke-width="2"><rect x="3" y="5" width="18" height="14" rx="1"/><path d="M3 6l9 7 9-7"/></svg>
            daniel.hayes@northgatebuild.com
          </li>
          <li>
            <svg viewBox="0 0 24 24" fill="none" stroke="#c47a4b" stroke-width="2"><path d="M12 22s7-7 7-12a7 7 0 0 0-14 0c0 5 7 12 7 12z"/><circle cx="12" cy="10" r="2.5"/></svg>
            48 Foundry Lane,<br>Riverton, CA 90410
          </li>
          <li><span class="social-dot"></span>@NorthgateBuild</li>
        </ul>
      </div>
    </div>
  </section>

</body>
</html>
```